Fitness Packaging

The attached box will be a new fitness product (see pictures). I need a graphic design for this box using the colors of black and yellow or black, yellow and silver. Please do not put any words, text, pictures of people, or any fitness equipment in the design. I just need your idea of an active, fitness, fun graphic design using the colors I mentioned. Please feel free to ask me any questions. Also, please see my "target market" section if it helps.

Measurements:

5.25" across

6" long or length

1 15/16" depth or deep

Cut out:

1 3/16" from top

3 5/8" from left

2 3/16" from bottom

Entire width of depth of right side is cut out

Cut out is 2 11/16" in length

Cut out is 1 5/8" cross missing from the front of the box

Cut out is 1 15/16" wide missing from the side

Hanging tag is 1 3/8" long

5 3/16 wide
Updates

Project Deadline Extended
Reason: I didn't get many design submissions.

Target Market(s)

Men and women (but maybe mostly men) from athletes to a Pearson who simply works out. Their age ranges will be between 19 years old to 40 years old. This product would have about the same target market (women can use also) as the Steady Lift-Bar https://steadyliftshop.example/product/Liftbar

Industry/Entity Type

Fitness Equipment

Colors
fbed22

Requirements
Must have
• Black and yellow or black, yellow, and silver
Should not have
• Please do not put any words, text, pictures of people, or any fitness equipment in the design

```html
<!DOCTYPE html>
<html lang="en">
<head>
<meta charset="utf-8">
<title>Fitness Packaging Dieline</title>
<link rel="stylesheet" href="https://fonts.googleapis.com/css2?family=Roboto&display=swap">
<style>
  :root {
    --paper: #ffffff;
    --brand-yellow: #fef100;
    --ink-black: #000000;
    --fold-line: #bdbdbd;
    --silver-light: #f2f2f2;
    --silver-mid: #c8c6c8;
    --silver-dark: #8a8488;
  }
  html, body {
    margin: 0;
    padding: 0;
    width: 1200px;
    height: 867px;
    overflow: hidden;
    background: var(--paper);
    font-family: "Roboto", sans-serif;
  }
  .dieline { display: block; width: 1200px; height: 867px; }
  .panel-yellow { fill: var(--brand-yellow); }
  .panel-black { fill: var(--ink-black); }
  .cutout { fill: var(--paper); }
  .fold { stroke: var(--fold-line); stroke-width: 1; fill: none; }
</style>
</head>
<body>
<svg class="dieline" viewBox="0 0 1300 940" role="img" aria-label="Flat dieline for a black, yellow and silver fitness box">
  <defs>
    <linearGradient id="silver-band" x1="0" x2="1" y1="0" y2="0">
      <stop offset="0" stop-color="var(--silver-light)"/>
      <stop offset="0.27" stop-color="var(--silver-dark)"/>
      <stop offset="0.5" stop-color="var(--silver-light)"/>
      <stop offset="0.7" stop-color="var(--silver-mid)"/>
      <stop offset="0.87" stop-color="var(--silver-dark)"/>
      <stop offset="1" stop-color="var(--silver-light)"/>
    </linearGradient>
  </defs>

  <!-- hang tag panel, top left -->
  <g class="hang-tag">
    <rect class="panel-yellow" x="105" y="29" width="375" height="234"/>
    <line class="fold" x1="105" y1="66" x2="480" y2="66"/>
    <line class="fold" x1="105" y1="164" x2="480" y2="164"/>
    <rect class="cutout" x="264" y="122" width="56" height="12" rx="6"/>
    <circle class="cutout" cx="292" cy="137" r="5"/>
    <rect class="cutout" x="264" y="193" width="56" height="13" rx="6"/>
    <circle class="cutout" cx="292" cy="190" r="5"/>
  </g>

  <!-- top dust flaps and lid -->
  <polygon class="panel-yellow top-flap" points="488,156 606,156 620,258 620,263 482,263 488,257"/>
  <rect class="panel-yellow top-lid" x="621" y="69" width="377" height="194"/>
  <line class="fold" x1="621" y1="124" x2="998" y2="124"/>
  <polygon class="panel-yellow top-flap" points="1014,155 1131,155 1131,258 1137,263 999,263 1000,258"/>

  <!-- yellow upper band of body -->
  <polygon class="panel-yellow upper-band" points="103,263 1138,263 1192,270 1192,324 103,324"/>

  <!-- silver divider band -->
  <rect class="silver-band" x="103" y="324" width="1089" height="20" fill="url(#silver-band)"/>

  <!-- black body panels -->
  <polygon class="panel-black body" points="103,344 1192,344 1192,688 1138,695 103,695"/>
  <rect class="panel-black tuck-tab" x="248" y="695" width="89" height="53"/>
  <rect class="fold" x="248" y="605" width="89" height="90"/>

  <!-- window cutout -->
  <rect class="cutout window" x="880" y="344" width="257" height="194"/>

  <!-- bottom flaps -->
  <polygon class="panel-black bottom-flap" points="482,695 620,695 606,802 488,802 488,701"/>
  <rect class="panel-black bottom-lid" x="621" y="695" width="377" height="193"/>
  <line class="fold" x1="621" y1="834" x2="998" y2="834"/>
  <rect class="cutout finger-slot" x="762" y="827" width="96" height="15" rx="7.5"/>
  <polygon class="panel-black bottom-flap" points="999,695 1137,695 1131,701 1131,802 1014,802"/>

  <!-- vertical folds -->
  <g class="folds">
    <line class="fold" x1="481" y1="263" x2="481" y2="695"/>
    <line class="fold" x1="621" y1="263" x2="621" y2="695"/>
    <line class="fold" x1="999" y1="538" x2="999" y2="695"/>
    <line class="fold" x1="999" y1="263" x2="999" y2="324"/>
    <line class="fold" x1="1138" y1="263" x2="1138" y2="695"/>
    <line class="fold" x1="103" y1="695" x2="1138" y2="695"/>
  </g>
</svg>
</body>
</html>
```